New Business Card for Software Company

We are looking at rebranding a 10 year old company that specializes in PDF and DWF solutions for Architects and Engineers. We will attach the new company logo that we are going with so you can work with that and complimentary colors.
The sample information we would like on the business card is:
Gerald Pembrook
Vice President
4173 W. Tillman Avenue. STE 306
PMB#417
Halvern, NV 85316
866-392-7154 US Toll Free
123-581-3064 Cell
gpembrook@vextrolan.com
The old tag line that we had on the business cars was.
Delivering Dependable Drawing File Tools to Architects and Engineers Everywhere.
If you have an idea for a better tag line we are open to that also.
Updates
We would like to thank all of the Designers for their wonderful work. We apologize that we will not have the time to provide feedback to everyone. There is just so many innovative and professional designs that you have all created making our decision even harder.
Target Market(s)
Architects and Engineers
Industry/Entity Type
Business
Look and feel
Each slider illustrates characteristics of the customer's brand and the style your logo design should communicate.

```html
<!DOCTYPE html>
<html lang="en">
<head>
<meta charset="utf-8">
<title>Vextrolan Business Card</title>
<link href="https://fonts.googleapis.com/css2?family=Mulish:wght@400;600;800&display=swap" rel="stylesheet">
<style>
  :root {
    --stage: #1c1c1c;
    --card-dark: #2b2b2b;
    --card-white: #ffffff;
    --orange: #ee6a1f;
    --orange-light: #f7a11c;
    --red: #b3261e;
    --text-light: #e8e8e8;
    --text-muted: #c9c9c9;
  }
  * { box-sizing: border-box; margin: 0; padding: 0; }
  html, body { width: 1200px; height: 900px; overflow: hidden; }
  body {
    background: var(--stage);
    font-family: "Mulish", Arial, sans-serif;
    position: relative;
  }
  .card {
    position: absolute;
    width: 500px;
    height: 286px;
    border-radius: 26px;
    overflow: hidden;
    background: var(--card-dark);
    top: 307px;
  }
  .card-front { left: 60px; }
  .card-back { left: 640px; }

  /* Front */
  .front-top {
    position: absolute; left: 0; top: 0; width: 100%; height: 128px;
    background: var(--card-white);
  }
  .brand { position: absolute; display: flex; align-items: center; gap: 12px; }
  .brand-dot { width: 34px; height: 34px; border-radius: 50%; background: var(--orange); }
  .brand-name { font-weight: 800; color: var(--orange); letter-spacing: -0.5px; }
  .front-top .brand { left: 40px; top: 40px; }
  .front-top .brand-name { font-size: 46px; line-height: 1; }
  .accent-band {
    position: absolute; left: 0; top: 128px; width: 100%; height: 8px;
    background: var(--orange);
  }
  .accent-notch {
    position: absolute; left: 44px; top: 135px; width: 0; height: 0;
    border-left: 9px solid transparent; border-right: 9px solid transparent;
    border-top: 9px solid var(--orange);
  }
  .person { position: absolute; left: 40px; top: 158px; width: 218px; color: var(--text-light); font-size: 13px; line-height: 1.3; }
  .person-name { color: var(--orange); font-weight: 800; font-size: 18px; }
  .person-title { margin-bottom: 14px; }
  .contact { position: absolute; left: 266px; top: 156px; color: var(--text-light); font-size: 12.5px; line-height: 1.4; list-style: none; }
  .contact-label { color: var(--orange); }

  /* Back */
  .card-back .brand { left: 34px; top: 108px; }
  .card-back .brand-name { font-size: 36px; line-height: 1; }
  .tagline {
    position: absolute; left: 36px; top: 158px; width: 200px;
    color: var(--text-muted); font-size: 11.5px; line-height: 1.3; text-align: center;
  }
  .mark-area {
    position: absolute; right: 0; top: 0; width: 230px; height: 100%;
    background: linear-gradient(135deg, var(--red) 0%, var(--orange) 45%, var(--orange-light) 100%);
  }
</style>
</head>
<body>
  <section class="card card-front" aria-label="Business card front">
    <div class="front-top">
      <div class="brand"><span class="brand-dot"></span><span class="brand-name">Vextrolan</span></div>
    </div>
    <div class="accent-band"></div>
    <div class="accent-notch"></div>
    <div class="person">
      <p class="person-name">Gerald Pembrook</p>
      <p class="person-title">Vice President</p>
      <p>4173 W. Tillman Avenue. STE 306</p>
      <p>PMB#417</p>
      <p>Halvern, NV 85316</p>
    </div>
    <ul class="contact">
      <li><span class="contact-label">Toll Free:</span> 866-392-7154</li>
      <li><span class="contact-label">Cell:</span> 123-581-3064</li>
      <li><span class="contact-label">Email:</span> gpembrook@vextrolan.com</li>
      <li><span class="contact-label">Web:</span> www.vextrolan.com</li>
    </ul>
  </section>

  <section class="card card-back" aria-label="Business card back">
    <div class="brand"><span class="brand-name">Vextrolan</span></div>
    <p class="tagline">Delivering Dependable Drawing File Tools to Architects and Engineers Everywhere</p>
    <div class="mark-area" role="img" aria-label="Large decorative brand symbol in orange and red tones"></div>
  </section>
</body>
</html>
```